Willowmere Veterinary Practice including Nest2Nurse

We require a double-sided full colour tri-fold Brochure for Print.
Colour theme to in line with logo below

Written CONTENT below
Orphans
We can provide care and a new mother for orphan foals of any age, breed or size, from thoroughbreds and draft breeds to tiny ponies and even donkeys.
We have successfully fostered orphans from a few hours of age through to eight weeks, regardless of how long or if at all they were with their birth mother, and of previous fostering attempts.
We have the knowledge and experience to provide optimum nutrition and care to orphans during the brief period that they don’t have a mum, until their new foster mother is ready to take them.
Additionally we are a veterinary practice, and can provide diagnostics and therapeutics for compromised orphan foals such as plasma administration and health checks.

Mares
Nest2Nurse mares have been selected for mothering ability and temperament, and have all carried and raised at least one foal of their own. Many have already been successful foster mothers in one or more of the last five breeding seasons.
The mares are not currently pregnant and are given a carefully designed course of hormones to induce lactation when required. The milk produced is not colostrum, but is completely normal and equivalent to that which they would have had if the foal was theirs by birth.
There is published scientific information (in addition to our own experience and that of the owners of previous graduates of our programme) that growth and development of foals raised by induced lactation is identical to that of foals raised by their birth mothers.

Fostering
During the few days when the mare’s udder is developing, mare and foal are kept next separately but in close proximity, allowing bonding to begin and reducing stress on the orphan.
The fostering is completed once the mare has enough milk to feed the foal, and our experienced handlers ensure that joining the two goes smoothly.
Once they are together the mare completely accepts the foal as her own, and the foal can suckle freely – at this stage we continue to offer supplementary feeds until they are not needed.
The mare and foal are then a normal unit and can return to the foal owner’s care until weaning – ensuring optimum nutrition and behaviour for the foal and excellent outcomes in performance, relationships with other horses, and interaction with humans.

Complete Safety
Mares recognise their birth foal by scent - a unique bond established during the first few minutes of the foal’s life - and only a small percentage of mares who have lost their own foal will readily accept a substitute.
When a mare who has lost her birth foal is offered an orphan, it is very normal and common for her to respond with aggression - to the danger of the foal and the human handler.
Nest2Nurse mares have no birth foal in the current season, and are happy to adopt any foal who is placed close to them during the hormone treatment period.
This makes for total foal and handler safety.

Excellent Success Rate
After seven years of perfecting the fostering method, Nest2Nurse can claim total success: we have now documented almost 50 fosterings over the last five breeding seasons. We have never been entrusted with an orphan foal that we have not been able to provide with a beautiful foster mum.

Career Mothers
Being dedicated career mothers with no other job in life, our mares are free to accompany their new foals home and stay with them as long as required. No foals are weaned and left without a mother in our programme, and our beautiful mares who would otherwise not be bred, are given a foal every year and a wonderful lifelong purpose.

Every single orphan’s human family has admired and appreciated our beautiful mares, with many offering to give them a home for life. Each season as the orphans are weaned, we welcome our mares home to Willowmere to prepare for the next foal in need – a job they totally love! – just as if they were in a natural breeding situation.

Willowmere Vet Practice including Nest2Nurse
218 Pellbrook Lane
Tarrick. Vic. 3872

Phone 0491583620 or 0438261597

```html
<!DOCTYPE html>
<html lang="en">
<head>
<meta charset="utf-8">
<title>Willowmere Veterinary Practice – Tri-fold Brochure</title>
<link href="https://fonts.googleapis.com/css2?family=Lato:wght@400;700&family=Montserrat:wght@500;600;800&family=Oswald:wght@600&display=swap" rel="stylesheet">
<style>
  :root {
    --orange: #ef5a14;
    --orange-light: #f5892b;
    --charcoal: #2b2b2b;
    --charcoal-deep: #222222;
    --ink: #1c1c1c;
    --paper: #ffffff;
    --stage: #e4e4e4;
    --body-font: "Lato", sans-serif;
    --head-font: "Montserrat", sans-serif;
    --display-font: "Oswald", sans-serif;
  }
  * { box-sizing: border-box; margin: 0; padding: 0; }
  html, body { width: 1200px; height: 1200px; overflow: hidden; background: var(--stage); }
  .canvas { position: relative; width: 1200px; height: 1200px; }

  .sheet {
    position: absolute; left: 200px; width: 800px; height: 560px;
    background: var(--paper); overflow: hidden;
    box-shadow: 0 6px 16px rgba(0,0,0,.25);
    font-family: var(--body-font);
  }
  .sheet--outside { top: 24px; }
  .sheet--inside { top: 614px; }
  .sheet-art { position: absolute; inset: 0; width: 800px; height: 560px; }

  /* Outside */
  .about { position: absolute; left: 26px; top: 48px; width: 200px; color: #fff; }
  .about__title { font-family: var(--head-font); font-weight: 600; color: var(--orange); font-size: 13.5px; margin-bottom: 8px; }
  .about__text { font-size: 8.4px; line-height: 1.32; text-align: justify; }

  .contact { position: absolute; left: 266px; top: 78px; width: 270px; text-align: center; color: #fff; }
  .contact__title { font-family: var(--head-font); font-weight: 500; font-size: 14px; margin-bottom: 12px; letter-spacing: .3px; }
  .contact__icon { display: block; margin: 0 auto 6px; }
  .contact__line { font-size: 9.2px; line-height: 1.35; margin-bottom: 6px; }

  .brand { display: flex; align-items: center; gap: 8px; font-family: var(--body-font); font-weight: 400; color: var(--ink); }
  .brand__dot { width: 14px; height: 14px; border-radius: 50%; background: var(--orange); flex: none; }
  .brand--middle { position: absolute; left: 266px; top: 470px; width: 270px; justify-content: center; font-size: 23px; }
  .brand--cover { position: absolute; left: 560px; top: 28px; font-size: 23px; }
  .brand--back { position: absolute; left: 556px; top: 452px; width: 244px; justify-content: center; font-size: 21px; color: #fff; }
  .brand--back .brand__dot { background: #fff; }

  .cover-copy { position: absolute; left: 535px; top: 428px; width: 265px; text-align: center; }
  .cover-copy__title { font-family: var(--display-font); font-weight: 600; font-size: 21px; color: var(--ink); letter-spacing: .2px; }
  .cover-copy__lead { font-size: 11px; color: var(--ink); margin-top: 16px; }
  .cover-copy__phone { font-family: var(--head-font); font-weight: 800; font-size: 24px; color: var(--orange); margin-top: 2px; letter-spacing: .5px; }

  /* Inside */
  .column { position: absolute; color: var(--ink); }
  .column--left { left: 24px; top: 0; width: 214px; }
  .column--middle { left: 286px; top: 0; width: 176px; }
  .section { position: absolute; left: 0; width: 100%; }
  .section__title { font-family: var(--head-font); font-weight: 500; font-size: 12.5px; line-height: 1.2; margin-bottom: 3px; }
  .column--middle .section__title { font-weight: 600; }
  .section__text { font-size: 7.3px; line-height: 1.26; text-align: justify; }
  .section__text + .section__text { margin-top: 0; }
  .site-url { position: absolute; left: 28px; bottom: 30px; font-family: var(--head-font); font-size: 9.5px; letter-spacing: 1.6px; color: var(--ink); }

  .call { position: absolute; left: 556px; top: 488px; width: 244px; text-align: center; color: #fff; }
  .call__label { font-family: var(--head-font); font-weight: 500; font-size: 12px; }
  .call__phone { font-family: var(--head-font); font-weight: 800; font-size: 22px; letter-spacing: .6px; margin-top: 4px; }
</style>
</head>
<body>
<main class="canvas">

  <!-- Outside of the tri-fold -->
  <section class="sheet sheet--outside" aria-label="Brochure outside">
    <svg class="sheet-art" viewBox="0 0 800 560" aria-hidden="false">
      <defs>
        <linearGradient id="coverPhotoTone" x1="0" y1="0" x2="0.3" y2="1">
          <stop offset="0" stop-color="#f4efe8"/>
          <stop offset="0.25" stop-color="#c9a57a"/>
          <stop offset="0.7" stop-color="#8a5a2f"/>
          <stop offset="1" stop-color="#d99a45"/>
        </linearGradient>
        <linearGradient id="stablePhotoTone" x1="0" y1="0" x2="1" y2="1">
          <stop offset="0" stop-color="#6b5a45"/>
          <stop offset="0.45" stop-color="#8a8f80"/>
          <stop offset="1" stop-color="#3f6b62"/>
        </linearGradient>
        <linearGradient id="foldShade" x1="0" x2="1">
          <stop offset="0" stop-color="#ededed"/>
          <stop offset="0.15" stop-color="#ffffff"/>
        </linearGradient>
      </defs>
      <rect class="panel-dark" x="0" y="0" width="266" height="560" fill="#2f2f2f"/>
      <rect class="panel-dark" x="266" y="0" width="270" height="560" fill="#262626"/>
      <rect class="panel-light" x="535" y="0" width="265" height="560" fill="url(#foldShade)"/>

      <!-- middle white wave with orange & black sweeps -->
      <path d="M266 278 C360 300 460 378 545 380 C640 382 730 348 800 300 V560 H266 Z" fill="#ffffff"/>
      <path d="M266 268 C360 292 460 370 545 374 C640 378 730 340 800 292" fill="none" stroke="#111" stroke-width="5"/>
      <path d="M266 262 C330 270 400 300 450 330" fill="none" stroke="var(--orange)" stroke-width="7" stroke-linecap="round"/>

      <!-- cover photo area -->
      <path d="M535 0 H800 V300 C740 342 650 375 545 372 L535 372 Z" fill="url(#coverPhotoTone)" role="img" aria-label="Photo: a woman resting her face against a grey horse's head in warm evening light"/>
      <path d="M640 410 C700 405 760 390 800 350" fill="none" stroke="var(--orange)" stroke-width="6" stroke-linecap="round"/>
      <path d="M700 388 C740 380 775 365 800 340" fill="none" stroke="var(--orange-light)" stroke-width="3"/>

      <!-- left panel photo with orange sweep -->
      <path d="M0 318 C80 290 190 290 266 330 L266 560 H0 Z" fill="url(#stablePhotoTone)" role="img" aria-label="Photo: a veterinarian bottle-feeding an orphan foal in a stable"/>
      <path d="M0 312 C80 282 190 282 266 322" fill="none" stroke="#ffffff" stroke-width="4"/>
      <path d="M0 304 C90 270 200 268 300 288" fill="none" stroke="var(--orange)" stroke-width="7" stroke-linecap="round"/>
    </svg>

    <article class="about">
      <h2 class="about__title">ABOUT US</h2>
      <p class="about__text">We are thrilled to announce that we are launching our very own Willowmere Vet Practice, with Clara Hensley as our lead Vet. Clara needs no introduction to the equine community – as the previous owner of Ashgrove Farm Vet Clinic, with her husband Martin. We are confident that having our own veterinary facility on-site will ensure optimum care of the Sanctuary residents, and also allow us to help look after animals in the local communities of Tarrick, Kelvale, Brindlee and beyond...</p>
    </article>

    <address class="contact">
      <h2 class="contact__title">CONTACT US</h2>
      <svg class="contact__icon" width="10" height="13" viewBox="0 0 10 13"><path d="M5 12 C2 8 1 6 1 4.5 A4 4 0 0 1 9 4.5 C9 6 8 8 5 12 Z" fill="none" stroke="var(--orange)" stroke-width="1.2"/><circle cx="5" cy="4.6" r="1.4" fill="var(--orange)"/></svg>
      <p class="contact__line">218 Pellbrook Lane<br>Tarrick 3872 VIC</p>
      <svg class="contact__icon" width="11" height="11" viewBox="0 0 11 11"><path d="M2 1 L4 1 L5 3.5 L3.8 4.6 C4.5 6 5.2 6.8 6.5 7.3 L7.6 6 L10 7 L10 9 C10 9.6 9.5 10 9 10 C4.5 9.7 1.3 6.5 1 2 C1 1.4 1.4 1 2 1 Z" fill="var(--orange)"/></svg>
      <p class="contact__line">0438 261 597</p>
      <svg class="contact__icon" width="12" height="10" viewBox="0 0 12 10"><rect x="1" y="1" width="10" height="8" fill="none" stroke="var(--orange)" stroke-width="1.2"/><path d="M1 1 L6 5.5 L11 1" fill="none" stroke="var(--orange)" stroke-width="1.2"/></svg>
      <p class="contact__line">admin@willowmerevet.com.au</p>
    </address>

    <div class="brand brand--middle"><span class="brand__dot"></span><span class="brand__name">Willowmere</span></div>
    <div class="brand brand--cover"><span class="brand__dot"></span><span class="brand__name">Willowmere</span></div>

    <div class="cover-copy">
      <h1 class="cover-copy__title">COMPASSIONATE CARE</h1>
      <p class="cover-copy__lead">Please call for an appointment</p>
      <p class="cover-copy__phone">0438 261 597</p>
    </div>
  </section>

  <!-- Inside of the tri-fold -->
  <section class="sheet sheet--inside" aria-label="Brochure inside">
    <svg class="sheet-art" viewBox="0 0 800 560">
      <defs>
        <linearGradient id="foldLeft" x1="0" x2="1">
          <stop offset="0" stop-color="#ffffff"/>
          <stop offset="0.88" stop-color="#ffffff"/>
          <stop offset="1" stop-color="#e2e2e2"/>
        </linearGradient>
        <linearGradient id="fieldPhotoTone" x1="0" y1="0" x2="1" y2="1">
          <stop offset="0" stop-color="#5d6a70"/>
          <stop offset="0.45" stop-color="#3c4a3a"/>
          <stop offset="1" stop-color="#a08a74"/>
        </linearGradient>
        <linearGradient id="callBlock" x1="0" y1="0" x2="0" y2="1">
          <stop offset="0" stop-color="var(--orange-light)"/>
          <stop offset="1" stop-color="var(--orange)"/>
        </linearGradient>
      </defs>
      <rect x="0" y="0" width="266" height="560" fill="url(#foldLeft)"/>
      <rect x="266" y="0" width="534" height="560" fill="#ffffff"/>

      <path d="M520 0 H800 V560 H528 C470 420 448 220 520 0 Z" fill="url(#fieldPhotoTone)" role="img" aria-label="Photo: a young woman in a rain jacket standing with a chestnut foal and a dark pony"/>
      <path d="M520 0 C470 60 455 120 470 180" fill="none" stroke="var(--orange)" stroke-width="9" stroke-linecap="round"/>
      <path d="M470 230 C505 330 525 440 528 560" fill="none" stroke="var(--orange)" stroke-width="5" stroke-linecap="round"/>
      <path d="M510 0 C480 50 470 100 472 140" fill="none" stroke="var(--orange-light)" stroke-width="2"/>

      <path d="M528 560 C560 470 650 420 800 368 V560 Z" fill="url(#callBlock)"/>
    </svg>

    <div class="column column--left">
      <section class="section" style="top:20px">
        <h2 class="section__title">ORPHANS</h2>
        <p class="section__text">We can provide care and a new mother for orphan foals of any age, breed or size, from thoroughbreds and draft breeds to tiny ponies and even donkeys. We have successfully fostered orphans from a few hours of age through to eight weeks, regardless of how long or if at all they were with their birth mother, and of previous fostering attempts. We have the knowledge and experience to provide optimum nutrition and care to orphans during the brief period that they don’t have a mum, until their new foster mother is ready to take them. Additionally we are a veterinary practice, and can provide diagnostics and therapeutics for compromised orphan foals such as plasma administration and health checks.</p>
      </section>
      <section class="section" style="top:180px">
        <h2 class="section__title">MARES</h2>
        <p class="section__text">Nest2Nurse mares have been selected for mothering ability and temperament, and have all carried and raised at least one foal of their own. Many have already been successful foster mothers in one or more of the last five breeding seasons. The mares are not currently pregnant, and are given a carefully designed course of hormones to induce lactation when required. The milk produced is not colostrum, but is completely normal and equivalent to that which they would have had if the foal was theirs by birth. There is published scientific information (in addition to our own experience and that of the owners of previous graduates of our programme) that growth and development of foals raised by induced lactation is identical to that of foals raised by their birth mothers.</p>
      </section>
      <section class="section" style="top:350px">
        <h2 class="section__title">FOSTERING</h2>
        <p class="section__text">During the few days when the mare’s udder is developing, mare and foal are kept separately but in close proximity, allowing bonding to begin and reducing stress on the orphan. The fostering is completed once the mare has enough milk to feed the foal, and our experienced handlers ensure that joining the two goes smoothly. Once they are together the mare completely accepts the foal as her own, and the foal can suckle freely – at this stage we continue to offer supplementary feeds until they are not needed. The mare and foal are then a normal unit and can return to the foal owner’s care until weaning.</p>
      </section>
    </div>
    <p class="site-url">willowmerevet.com.au</p>

    <div class="column column--middle">
      <section class="section" style="top:22px">
        <h2 class="section__title">COMPLETE SAFETY</h2>
        <p class="section__text">Mares recognise their birth foal by scent - a unique bond established during the first few minutes of the foal’s life - and only a small percentage of mares who have lost their own foal will readily accept a substitute. When a mare who has lost her birth foal is offered an orphan, it is very normal and common for her to respond with aggression - to the danger of the foal and the human handler. Nest2Nurse mares have no birth foal in the current season, and are happy to adopt any foal who is placed close to them during the hormone treatment period. This makes for total foal and handler safety.</p>
      </section>
      <section class="section" style="top:212px">
        <h2 class="section__title">EXCELLENT SUCCESS<br>RATE</h2>
        <p class="section__text">After seven years of perfecting the fostering method, Nest2Nurse can claim total success: we have now documented almost 50 fosterings over the last five breeding seasons. We have never been entrusted with an orphan foal that we have not been able to provide with a beautiful foster mum.</p>
      </section>
      <section class="section" style="top:328px">
        <h2 class="section__title">CAREER MOTHERS</h2>
        <p class="section__text" style="margin-top:10px">Being dedicated career mothers with no other job in life, our mares are free to accompany their new foals home and stay with them as long as required. No foals are weaned and left without a mother in our programme, and our beautiful mares who would otherwise not be bred, are given a foal every year and a wonderful lifelong purpose. Every single orphan’s human family has admired and appreciated our beautiful mares, with many offering to give them a home for life. Each season as the orphans are weaned, we welcome our mares home to Willowmere to prepare for the next foal in need – a job they totally love! – just as if they were in a natural breeding situation.</p>
      </section>
    </div>

    <div class="brand brand--back"><span class="brand__dot"></span><span class="brand__name">Willowmere</span></div>
    <div class="call">
      <p class="call__label">CALL US</p>
      <p class="call__phone">0438 261 597</p>
    </div>
  </section>

</main>
</body>
</html>
```